Business Card Design

I design and sell kitchens. I would like the card to have a black background either gloss or matt and a stripe through the middle in deep sky blue, the same blue as the team lark pro cycling team. Written in the blue stripe in white i would like Meridian kitchens in italics. underneath the stripe, again in white i would like 'the complete design and installation service. On the reverse i would like the following in simple black on white
Dean Marwick
07841 296054
email- deanmarwick@meridiankitchens-example.co.uk
Web- WWW.meridiankitchens-example.co.uk

I have added a copy of an initial idea for a logo but it can be changed to suit the brief above

Industry/Entity Type

Business

Contact Information for Business Card

Meridian Kitchens
The complete design and installation service
Dean Marwick
07841 296054-mob
deanmarwick@meridiankitchen-example.co.uk
WWW.meridiankitchens-example.co.uk

```html
<!DOCTYPE html>
<html lang="en">
<head>
<meta charset="utf-8">
<title>Meridian Kitchens – Business Card</title>
<link rel="stylesheet" href="https://fonts.googleapis.com/css2?family=Open+Sans:ital,wght@0,400;0,800;1,400&display=swap">
<style>
  :root {
    --sky: #0cb0e6;
    --card-black: #111111;
    --paper: #ffffff;
    --ink: #1a1a1a;
    --backdrop: #e9e7e4;
    --kitchen-light: #d9d2ca;
    --kitchen-mid: #9c8b7d;
    --kitchen-dark: #5e5048;
  }
  * { box-sizing: border-box; margin: 0; padding: 0; }
  html, body {
    width: 1200px; height: 1023px; overflow: hidden;
    background: var(--backdrop);
    font-family: "Open Sans", Arial, sans-serif;
  }
  .sheet {
    width: 1200px; height: 1023px;
    display: flex; flex-direction: column;
    align-items: center; justify-content: center; gap: 56px;
  }
  .card {
    position: relative;
    width: 760px; height: 434px;
    overflow: hidden;
    box-shadow: 0 6px 18px rgba(0,0,0,.18);
  }

  /* Front: black card with a sky-blue stripe */
  .card--front { background: var(--card-black); }
  .stripe {
    position: absolute; left: 0; right: 0; top: 132px; height: 150px;
    background: var(--sky);
    display: flex; align-items: center; justify-content: center;
  }
  .stripe .brand { color: var(--paper); font-size: 64px; }
  .brand {
    font-weight: 800; line-height: 1.0; letter-spacing: -1px;
  }
  .tagline {
    position: absolute; left: 0; right: 0; top: 306px;
    text-align: center;
    color: var(--paper); font-size: 25px; font-weight: 400; font-style: italic;
  }

  /* Back */
  .card--back { background: var(--paper); }
  .card--back .brand {
    position: absolute; left: 40px; top: 44px;
    color: var(--sky); font-size: 70px;
  }
  .kitchen-photo {
    position: absolute; right: 0; top: 0;
    width: 380px; height: 100%;
    background:
      linear-gradient(90deg, var(--paper) 0%, rgba(255,255,255,0) 40%),
      linear-gradient(180deg, var(--kitchen-mid) 0%, var(--kitchen-dark) 40%, var(--kitchen-light) 58%, var(--kitchen-mid) 78%, #ece8e4 100%);
  }
  .contact {
    position: absolute; left: 40px; bottom: 26px;
    color: var(--ink);
  }
  .contact__name {
    color: var(--sky); font-style: italic; font-weight: 400;
    font-size: 28px; margin-bottom: 8px;
  }
  .contact__line {
    display: flex; align-items: center; gap: 8px;
    font-style: italic; font-size: 21px; line-height: 1.55;
  }
  .contact__icon { width: 20px; height: 20px; flex: none; }
</style>
</head>
<body>
<main class="sheet">

  <section class="card card--front" aria-label="Card front">
    <div class="stripe">
      <div class="brand">Meridian Kitchens</div>
    </div>
    <p class="tagline">The complete design and installation service</p>
  </section>

  <section class="card card--back" aria-label="Card back">
    <div class="kitchen-photo" role="img" aria-label="Photograph of a modern kitchen with a marble island and wooden bar stools"></div>
    <div class="brand">Meridian<br>Kitchens</div>
    <div class="contact">
      <p class="contact__name">Dean Marwick</p>
      <p class="contact__line">
        <svg class="contact__icon" viewBox="0 0 20 20" aria-hidden="true">
          <circle cx="10" cy="10" r="10" fill="var(--sky)"/>
          <rect x="7" y="4.5" width="6" height="11" rx="1.2" fill="none" stroke="#fff" stroke-width="1.4"/>
          <circle cx="10" cy="13.3" r=".8" fill="#fff"/>
        </svg>
        07841 296054
      </p>
      <p class="contact__line">
        <svg class="contact__icon" viewBox="0 0 20 20" aria-hidden="true">
          <circle cx="10" cy="10" r="10" fill="var(--sky)"/>
          <rect x="5" y="6.5" width="10" height="7" fill="#fff"/>
          <path d="M5 6.5 L10 10.8 L15 6.5" fill="none" stroke="var(--sky)" stroke-width="1.2"/>
        </svg>
        deanmarwick@meridiankitchens-example.co.uk
      </p>
      <p class="contact__line">
        <svg class="contact__icon" viewBox="0 0 20 20" aria-hidden="true">
          <circle cx="10" cy="10" r="10" fill="var(--sky)"/>
          <g fill="none" stroke="#fff" stroke-width="1.2">
            <circle cx="10" cy="10" r="5.5"/>
            <ellipse cx="10" cy="10" rx="2.4" ry="5.5"/>
            <path d="M4.5 10 H15.5"/>
          </g>
        </svg>
        www.meridiankitchens-example.co.uk
      </p>
    </div>
  </section>

</main>
</body>
</html>
```